Web template for real estate developing company
KORVALD
Real Estate
www.morvinkorvald.dk
Developing real estate company in Denmark.
Consulting Competence
Handling of a project:
Analysis of local conditions and market analysis
Functional and usability concept
Analysis of profitability
Financing and utilization strategies
Economic and Technical project control
Like: Start up movement on the KORVALD logo like a dynamic building assamply on a black/grey background.
Dont like: To much information and pictures on the first front page.
Elegant
black background
grey backgrund
red logo
top
http://www.lindquistaro.com/
We want to have total remake on our website www.morvinkorvald.dk .
the design and setup on this brochure can be an inspiration
logo
Please place the above jpg-photos in decending order.

```html
<!DOCTYPE html>
<html lang="da">
<head>
<meta charset="utf-8">
<title>KORVALD – Real Estate</title>
<link rel="stylesheet" href="https://fonts.googleapis.com/css2?family=Roboto+Condensed:wght@400;700&display=swap">
<style>
  :root {
    --black: #0b0b0b;
    --night: #1a1a1a;
    --steel: #8e8e8e;
    --steel-light: #b4b4b4;
    --steel-dark: #6f6f6f;
    --paper: #d9d9d9;
    --red: #e01b2f;
    --red-deep: #b8101f;
    --ink: #222222;
    --white: #ffffff;
  }
  * { margin: 0; padding: 0; box-sizing: border-box; }
  html, body { width: 1200px; height: 559px; overflow: hidden; background: var(--black); }
  body { font-family: "Roboto Condensed", Arial, sans-serif; }

  .page { position: relative; width: 1200px; height: 559px; overflow: hidden;
          background: linear-gradient(180deg, #151515 0%, var(--black) 100%); }

  .top-band { position: absolute; left: 187px; top: 0; width: 1013px; height: 24px; background: var(--red); }

  .stage { position: absolute; left: 0; top: 0; }

  .header-logo { position: absolute; left: 187px; top: 24px; width: 250px; height: 116px;
                 background: linear-gradient(180deg, #eeeeee, var(--paper)); }
  .brand { position: absolute; left: 200px; top: 60px; display: flex; align-items: center; gap: 12px; }
  .brand-mark { width: 40px; height: 40px; background: var(--red); }
  .brand-name { font-weight: 700; font-size: 38px; letter-spacing: 1px; color: var(--ink); }

  .main-nav { position: absolute; left: 448px; top: 104px; display: flex; gap: 26px; }
  .main-nav a { position: relative; color: var(--white); text-decoration: none; font-size: 16px;
                letter-spacing: 0.5px; text-transform: uppercase; }
  .main-nav a.is-active::after { content: ""; position: absolute; left: -6px; right: -6px; top: 26px;
                height: 4px; background: var(--red); }
  .main-nav a.is-active::before { content: ""; position: absolute; left: 50%; top: 30px; margin-left: -6px;
                border: 6px solid transparent; border-top-color: var(--red); }

  .contact-card { position: absolute; left: 240px; top: 451px; width: 326px; height: 78px;
                  background: var(--red); color: var(--white); padding: 9px 14px; line-height: 1.25; }
  .contact-card p { font-size: 12px; }
  .contact-card .phone { font-size: 19px; font-weight: 700; }
  .contact-card .phone span { font-size: 12px; font-weight: 400; margin-left: 8px; }
</style>
</head>
<body>
<div class="page">
  <div class="top-band"></div>

  <svg class="stage" width="1200" height="559" viewBox="0 0 1200 559" aria-hidden="false">
    <defs>
      <linearGradient id="panel" x1="0" y1="0" x2="1" y2="1">
        <stop offset="0" stop-color="#a3a3a3"/>
        <stop offset="1" stop-color="#7a7a7a"/>
      </linearGradient>
      <linearGradient id="photo" x1="0" y1="0" x2="1" y2="1">
        <stop offset="0" stop-color="#e6e6e6"/>
        <stop offset="0.55" stop-color="#9aa0a6"/>
        <stop offset="1" stop-color="#b58a4e"/>
      </linearGradient>
    </defs>
    <polygon points="187,24 1200,24 1200,523 580,523 187,262" fill="url(#panel)"/>
    <polygon points="187,140 1200,140 1200,360 560,523 470,523 187,330" fill="#ffffff" opacity="0.08"/>
    <rect x="187" y="523" width="1013" height="36" fill="var(--night)"/>
    <g class="photo-tiles" role="img" aria-label="Construction site photographs set in diamond tiles">
      <polygon points="396,170 464,238 396,306 328,238" fill="url(#photo)"/>
      <polygon points="547,165 615,233 547,301 479,233" fill="url(#photo)"/>
      <polygon points="713,160 781,228 713,296 645,228" fill="url(#photo)"/>
      <polygon points="864,165 932,233 864,301 796,233" fill="url(#photo)"/>
      <polygon points="470,237 538,305 470,373 402,305" fill="url(#photo)"/>
      <polygon points="624,235 692,303 624,371 556,303" fill="url(#photo)"/>
      <polygon points="787,235 855,303 787,371 719,303" fill="url(#photo)"/>
      <polygon points="936,237 1004,305 936,373 868,305" fill="url(#photo)"/>
      <polygon points="542,304 610,372 542,440 474,372" fill="url(#photo)"/>
      <polygon points="700,304 768,372 700,440 632,372" fill="url(#photo)"/>
      <polygon points="859,304 927,372 859,440 791,372" fill="url(#photo)"/>
    </g>
  </svg>

  <div class="header-logo"></div>
  <div class="brand">
    <span class="brand-mark"></span>
    <span class="brand-name">KORVALD</span>
  </div>

  <nav class="main-nav">
    <a href="#" class="is-active">Forside</a>
    <a href="#">Projektudvikling</a>
    <a href="#">Referencer</a>
    <a href="#">Økonomi</a>
    <a href="#">Presse</a>
    <a href="#">Kontakt</a>
  </nav>

  <address class="contact-card">
    <p>Holmevej 22, 7100 Vejle, Danmark</p>
    <p class="phone">Tlf.: 76 42 18 30<span>www.morvinkorvald.dk</span></p>
    <p>Mail: post@morvinkorvald.dk</p>
  </address>
</div>
</body>
</html>
```